New Design for our Velorin Gran Reserva Brandy, it is the label design for the bottle label

We need a new bottle label for our Brandy Gran Reserva that we want to bring to the market.

Please have a look at all our current bottles and labels and the feel of our company under www.velorin-example.ch

The bottle that we will be using for the brand is a different one than the one that we already have, the design of the bottle is attached with a document.

I have also attached a briefing in regards to Brandy in general for your information.

### 1. What is Brandy?
Brandy is a distilled spirit made from fermented wine or other fruit wines. It is traditionally aged in oak barrels, which gives it its characteristic color and rich flavor. The aging process in oak is essential for developing the aromas and quality of the brandy.

### 2. What is Brandy Reserva?
A Brandy labeled as "Reserva" has undergone a longer aging process, typically at least 2 to 3 years, in oak barrels. This aging gives the brandy a deeper, more complex flavor profile and a darker color. "Reserva" is often an indication of higher quality.

### 3. Who enjoys drinking Brandy?
Brandy is typically favored by those who appreciate a deep, rich tasting experience. This often includes older consumers who value the time-aged complexity of the spirit. However, Brandy is also gaining popularity among younger people, especially through cocktails and modern serving styles.

### 4. Why is Brandy trending?
Brandy is experiencing a resurgence as consumers increasingly value quality and artisanal production methods. Its versatility in cocktails and association with traditional, luxurious experiences have also contributed to its renewed popularity.

### 5. What colors would be associated with Brandy?
The typical colors associated with Brandy are warm gold, amber, and deep golden-brown tones. These colors reflect the aging process in oak barrels and the richness of the flavors. Other associated colors might include dark brown and mahogany.

### 6. What is important to customers when buying Brandy?
Customers care about the origin of the Brandy, the aging time, the quality of the ingredients, the production method, and the brand. They also pay attention to the prestige of the product and the authenticity of the production.

### 7. What is not important to customers when buying Brandy?
For many customers, the price and packaging (unless it’s especially exclusive) may be less important than the quality and taste of the Brandy. The distillery name might be less significant if it isn’t tied to a particular reputation.

### 8. What do customers know about Swiss Brandy?
Swiss Brandy is still relatively unknown in many markets, but customers who are familiar with it appreciate the precision and quality of Swiss production. Swiss Brandy is assumed to be made with care and under strict quality standards.

### 9. What is Brandy Gran Reserva?
**Brandy Gran Reserva** is an even higher quality and longer-aged version of Brandy. Generally, a Gran Reserva is aged for at least 5 to 10 years or more in oak barrels. This extended aging process gives the Brandy an especially deep, complex flavor profile and often a darker, richer color. Gran Reserva is often regarded as the top-tier product within a Brandy range and appeals to discerning consumers who value quality, refinement, and a luxurious tasting experience.

The label “Gran Reserva” thus indicates the highest quality level for Brandies, similar to other spirits (like wine or whisky), where the aging time is a critical factor.

### 10. What emotions are associated with Brandy?
Brandy is often associated with luxury, relaxation, and comfort. It evokes feelings of tradition, elegance, and sophistication. Drinking Brandy is frequently seen as a moment of reflection and enjoyment.

### 11. How should Brandy be marketed?
Brandy should be marketed with a focus on its artisanal production, quality, and tradition. A narrative around the product, its aging, and origin can help create an emotional connection with the customer. The marketing should also emphasize the versatility of Brandy, whether consumed neat or in cocktails.

### 12. Sales test and label design for Velorin Brandy
For a sales test, I would suggest a tasting in an upscale setting, perhaps paired with a storytelling presentation highlighting the history of the 6-year aged Brandy and its aging in oak barrels.

**Label design**:
The label should reflect the exclusivity of the product, with an elegant, minimalist design. Colors like deep gold, mahogany, and a hint of deep blue could be used to emphasize the aging and quality of the Brandy. The label should include information about the aging time, the use of oak barrels, and a brief story about the Brandy’s production. A seal or embossing highlighting the craftsmanship would also be fitting.

Target Market(s)

Customers that like Brandy

Requirements
Must have
• the Alcohol % must be included on the label as well as our address.

```html
<!DOCTYPE html>
<html lang="en">
<head>
<meta charset="utf-8">
<title>Velorin Gran Reserva – Bottle Label</title>
<link rel="stylesheet" href="https://fonts.googleapis.com/css2?family=Marcellus&family=Italiana&family=Gloock&family=Montserrat:wght@400;800&display=swap">
<style>
  :root {
    --page: #ffffff;
    --die-cut: #d3d5d7;
    --label-cream: #fbf3ea;
    --frame-brown: #4e1c14;
    --rule-brown: #6b3a22;
    --ink-navy: #1d2b4a;
    --ink-muted: #4a3a48;
    --gold: #c9a227;
    --sketch-light: #e9d8c8;
    --sketch-dark: #8a5a4a;
  }
  html, body {
    margin: 0;
    padding: 0;
    width: 675px;
    height: 1200px;
    overflow: hidden;
    background: var(--page);
  }
  .label-canvas {
    display: block;
    width: 675px;
    height: 1200px;
  }
  .die-cut { fill: var(--die-cut); }
  .label-body { fill: var(--label-cream); stroke: var(--frame-brown); stroke-width: 8; }
  .stitch-line { fill: none; stroke: var(--frame-brown); stroke-width: 2; stroke-dasharray: 9 6; }
  .double-rule { stroke: var(--frame-brown); stroke-width: 3; }
  .dot-rule { stroke: var(--rule-brown); stroke-width: 2.5; }
  .dot-rule-end { fill: var(--rule-brown); }
  .corner-ornament { fill: var(--sketch-light); }
  .gold-flourish { fill: var(--gold); opacity: 0.55; }
  .brand-name {
    font-family: "Marcellus", serif;
    font-size: 84px;
    letter-spacing: 4px;
    fill: var(--frame-brown);
  }
  .grade {
    font-family: "Marcellus", serif;
    font-size: 50px;
    fill: var(--ink-navy);
  }
  .aging-method {
    font-family: "Italiana", serif;
    font-size: 48px;
    letter-spacing: 5px;
    fill: var(--ink-navy);
  }
  .age-statement {
    font-family: "Gloock", serif;
    font-size: 68px;
    fill: var(--ink-navy);
  }
  .origin {
    font-family: "Montserrat", sans-serif;
    font-weight: 800;
    font-size: 26px;
    letter-spacing: 3px;
    fill: var(--ink-navy);
  }
  .craft-note {
    font-family: "Italiana", serif;
    font-size: 23px;
    letter-spacing: 1.5px;
    fill: var(--ink-muted);
  }
  .story-text {
    font-family: "Montserrat", sans-serif;
    font-weight: 400;
    font-size: 14.5px;
    letter-spacing: 1px;
    fill: var(--ink-navy);
  }
</style>
</head>
<body>
<svg class="label-canvas" viewBox="0 0 1456 2588" xmlns="http://www.w3.org/2000/svg" aria-label="Velorin Gran Reserva brandy label">
  <defs>
    <linearGradient id="sketch-tone" x1="0" y1="0" x2="1" y2="1">
      <stop offset="0" stop-color="#efe2d4"/>
      <stop offset="1" stop-color="#c9a494"/>
    </linearGradient>
    <path id="label-outline" d="M 545 480 Q 725 336 910 480 L 957 480 L 957 500 Q 957 525 982 525 L 1000 525 L 1000 640 C 1078 780 1078 1180 1000 1320 L 1000 1440 L 982 1440 Q 957 1440 957 1465 L 957 1485 L 910 1485 Q 725 1627 545 1485 L 497 1485 L 497 1465 Q 497 1440 472 1440 L 454 1440 L 454 1320 C 376 1180 376 780 454 640 L 454 525 L 472 525 Q 497 525 497 500 L 497 480 Z"/>
  </defs>

  <!-- Die-cut sheet -->
  <polygon class="die-cut" points="293,349 1155,349 1065,1610 384,1610"/>

  <!-- Label shape -->
  <use href="#label-outline" class="label-body"/>
  <use href="#label-outline" class="stitch-line" transform="translate(725 982) scale(0.945 0.958) translate(-725 -982)"/>

  <!-- Brand block -->
  <g class="brand-block">
    <line class="double-rule" x1="572" y1="540" x2="875" y2="540"/>
    <line class="double-rule" x1="572" y1="546" x2="875" y2="546"/>
    <rect class="corner-ornament" x="515" y="528" width="54" height="52" rx="10" role="img" aria-label="Flourish ornament"/>
    <rect class="corner-ornament" x="878" y="528" width="54" height="52" rx="10" role="img" aria-label="Flourish ornament"/>
    <text class="brand-name" x="718" y="630" text-anchor="middle">VELORIN</text>
    <rect class="corner-ornament" x="515" y="632" width="54" height="52" rx="10" role="img" aria-label="Flourish ornament"/>
    <rect class="corner-ornament" x="878" y="632" width="54" height="52" rx="10" role="img" aria-label="Flourish ornament"/>
    <line class="double-rule" x1="572" y1="664" x2="875" y2="664"/>
    <line class="double-rule" x1="572" y1="670" x2="875" y2="670"/>
  </g>

  <!-- Product details -->
  <text class="grade" x="720" y="720" text-anchor="middle">GRAN RESERVA</text>

  <line class="dot-rule" x1="566" y1="740" x2="882" y2="740"/>
  <circle class="dot-rule-end" cx="566" cy="740" r="5"/>
  <circle class="dot-rule-end" cx="882" cy="740" r="5"/>

  <text class="aging-method" x="727" y="785" text-anchor="middle">Oak Barrel Aging</text>

  <line class="dot-rule" x1="541" y1="814" x2="906" y2="814"/>
  <circle class="dot-rule-end" cx="541" cy="814" r="6"/>
  <circle class="dot-rule-end" cx="906" cy="814" r="6"/>

  <text class="age-statement" x="711" y="876" text-anchor="middle">6 YEARS AGED</text>

  <line class="dot-rule" x1="537" y1="888" x2="902" y2="888"/>
  <circle class="dot-rule-end" cx="537" cy="888" r="6"/>
  <circle class="dot-rule-end" cx="902" cy="888" r="6"/>

  <text class="origin" x="732" y="926" text-anchor="middle">Swiss Brandy</text>

  <rect class="gold-flourish" x="563" y="970" width="327" height="22" rx="11" role="img" aria-label="Gold flourish divider"/>

  <!-- Illustration area -->
  <rect x="583" y="1023" width="288" height="292" rx="40" fill="url(#sketch-tone)" role="img" aria-label="Sepia sketch of an oak barrel with a bottle, a wine glass and grapes"/>

  <text class="craft-note" x="724" y="1362" text-anchor="middle">Handcrafted</text>

  <text class="story-text" text-anchor="middle">
    <tspan x="727" y="1404">Lorem Ipsum is simply dummy text of the</tspan>
    <tspan x="727" y="1421">printing and typesetting industry. Lorem</tspan>
    <tspan x="727" y="1438">Ipsum has been the industry's standard</tspan>
    <tspan x="727" y="1455">dummy text ever since the 1500s,</tspan>
  </text>
</svg>
</body>
</html>
```